Business Card Ayurvedic Massage

I'm starting with my ayurvedic massage business and need a business card design. The design should be inline with my brand/logo as well as with the design of my website (www.lumo-thara.ch).
Front: logo and text "Ayurvedische Massagen"
back: name and adress (see details https://www.lumo-thara.ch/kontakt.html)

```html
<!DOCTYPE html>
<html lang="de">
<head>
<meta charset="utf-8">
<title>lumo-thara – Visitenkarte</title>
<link rel="stylesheet" href="https://fonts.googleapis.com/css2?family=Tinos&family=Yatra+One&family=Open+Sans:wght@400&display=swap">
<style>
  :root {
    --navy: #253044;
    --divider: #7a1518;
    --card-red: #7d1418;
    --card-red-deep: #5e0e12;
    --gold: #e3b449;
    --gold-deep: #b57a1c;
    --cream: #efdfc4;
    --maroon: #7a1a1a;
    --ornament-text: #5c5848;
    --ornament-tint: #e2c9b0;
  }
  * { margin: 0; padding: 0; box-sizing: border-box; }
  html, body { width: 1200px; height: 672px; overflow: hidden; }
  body { background: var(--navy); position: relative; }

  .divider {
    position: absolute; left: 594px; top: 0; width: 12px; height: 672px;
    background: var(--divider);
  }

  .card {
    position: absolute; width: 537px; border-radius: 18px; overflow: hidden;
  }
  .card--left { left: 28px; }
  .card--right { left: 638px; }

  /* Front */
  .card-front {
    top: 20px; height: 304px;
    background: radial-gradient(ellipse at center, var(--card-red) 0%, var(--card-red-deep) 100%);
  }
  .elephant {
    position: absolute; top: 60px; width: 120px; height: 154px; border-radius: 10px;
    background: linear-gradient(160deg, var(--gold) 0%, var(--gold-deep) 100%);
    opacity: 0.85;
  }
  .elephant--left { left: 40px; }
  .elephant--right { left: 377px; }
  .brand-name {
    position: absolute; left: 160px; width: 217px; top: 131px;
    text-align: center; color: var(--gold); white-space: nowrap;
    font-family: "Tinos", serif; font-size: 40px; line-height: 46px;
  }
  .front-tagline {
    position: absolute; left: 0; right: 0; top: 224px; text-align: center;
    color: var(--gold); font-family: "Tinos", serif; font-size: 20.5px; line-height: 24px;
  }

  /* Back */
  .card-back {
    top: 342px; height: 304px; background: var(--cream);
  }
  .ornament {
    position: absolute; left: 172px; width: 192px; height: 38px; border-radius: 6px;
    background: var(--ornament-tint);
  }
  .ornament--top { top: 6px; }
  .ornament--bottom { top: 97px; }
  .back-tagline {
    position: absolute; left: 0; right: 0; top: 49px; text-align: center;
    color: var(--ornament-text); font-family: "Tinos", serif; font-size: 20px; line-height: 23px;
  }
  .contact-list { list-style: none; }
  .contact-item {
    position: absolute; left: 16px; right: 8px;
    display: flex; align-items: flex-start; color: var(--maroon);
  }
  .contact-icon { width: 22px; height: 22px; flex: none; margin-right: 14px; margin-top: 1px; }
  .contact-icon path { fill: var(--maroon); }
  .contact-item--address { top: 142px; }
  .contact-item--phone { top: 199px; }
  .contact-item--web { top: 232px; }
  .contact-item--mail { top: 268px; }

  .contact-text { line-height: 25px; white-space: nowrap; }
  .card--left .contact-text {
    font-family: "Yatra One", cursive; font-size: 21px; text-transform: lowercase;
  }
  .card--right .contact-text {
    font-family: "Open Sans", sans-serif; font-size: 23px;
  }
</style>
</head>
<body>
  <div class="divider"></div>

  <section class="card card-front card--left">
    <div class="elephant elephant--left" role="img" aria-label="Geschmückter goldener Elefant mit Schirm"></div>
    <div class="brand-name">lumo-thara</div>
    <div class="elephant elephant--right" role="img" aria-label="Geschmückter goldener Elefant mit Schirm"></div>
    <p class="front-tagline">AYURVEDISCHE MASSAGEN</p>
  </section>

  <section class="card card-front card--right">
    <div class="elephant elephant--left" role="img" aria-label="Geschmückter goldener Elefant mit Schirm"></div>
    <div class="brand-name">lumo-thara</div>
    <div class="elephant elephant--right" role="img" aria-label="Geschmückter goldener Elefant mit Schirm"></div>
    <p class="front-tagline">AYURVEDISCHE MASSAGEN</p>
  </section>

  <section class="card card-back card--left">
    <div class="ornament ornament--top" role="img" aria-label="Blattornament"></div>
    <p class="back-tagline">AYURVEDISCHE<br>MASSAGEN</p>
    <div class="ornament ornament--bottom" role="img" aria-label="Blattornament"></div>
    <ul class="contact-list">
      <li class="contact-item contact-item--address">
        <svg class="contact-icon" viewBox="0 0 24 24"><path d="M12 2a7 7 0 0 0-7 7c0 5 7 13 7 13s7-8 7-13a7 7 0 0 0-7-7zm0 9.5A2.5 2.5 0 1 1 12 6.5a2.5 2.5 0 0 1 0 5z"/></svg>
        <span class="contact-text">Mira Talven, lumo-thara, Lindenweg 14,<br>8857 Vorderthal (SZ)</span>
      </li>
      <li class="contact-item contact-item--phone">
        <svg class="contact-icon" viewBox="0 0 24 24"><path d="M6.6 10.8a15 15 0 0 0 6.6 6.6l2.2-2.2c.3-.3.7-.4 1-.2 1.1.4 2.3.6 3.6.6.6 0 1 .4 1 1V20c0 .6-.4 1-1 1A17 17 0 0 1 3 4c0-.6.4-1 1-1h3.5c.6 0 1 .4 1 1 0 1.3.2 2.5.6 3.6.1.3 0 .7-.2 1z"/></svg>
        <span class="contact-text">+41 77 000 12 34 (Bitte keine Werbung)</span>
      </li>
      <li class="contact-item contact-item--web">
        <svg class="contact-icon" viewBox="0 0 24 24"><path d="M12 2a10 10 0 1 0 0 20 10 10 0 0 0 0-20zm6.9 6h-3a15 15 0 0 0-1.3-3.9A8 8 0 0 1 18.9 8zM12 4c.8 1.1 1.5 2.5 1.9 4h-3.8c.4-1.5 1.1-2.9 1.9-4zM4.3 14a8 8 0 0 1 0-4h3.4a16 16 0 0 0 0 4zm.8 2h3a15 15 0 0 0 1.3 3.9A8 8 0 0 1 5.1 16zm3-8h-3a8 8 0 0 1 4.3-3.9A15 15 0 0 0 8.1 8zM12 20c-.8-1.1-1.5-2.5-1.9-4h3.8c-.4 1.5-1.1 2.9-1.9 4zm2.3-6H9.7a14 14 0 0 1 0-4h4.6a14 14 0 0 1 0 4zm.3 5.9a15 15 0 0 0 1.3-3.9h3a8 8 0 0 1-4.3 3.9zm1.7-5.9a16 16 0 0 0 0-4h3.4a8 8 0 0 1 0 4z"/></svg>
        <span class="contact-text">www.lumo-thara.ch</span>
      </li>
      <li class="contact-item contact-item--mail">
        <svg class="contact-icon" viewBox="0 0 24 24"><path d="M3 5h18v14H3zm2 2v.5l7 4.5 7-4.5V7zm0 2.9V17h14V9.9l-7 4.5z"/></svg>
        <span class="contact-text">info@lumo-thara.ch</span>
      </li>
    </ul>
  </section>

  <section class="card card-back card--right">
    <div class="ornament ornament--top" role="img" aria-label="Blattornament"></div>
    <p class="back-tagline">AYURVEDISCHE<br>MASSAGEN</p>
    <div class="ornament ornament--bottom" role="img" aria-label="Blattornament"></div>
    <ul class="contact-list">
      <li class="contact-item contact-item--address">
        <svg class="contact-icon" viewBox="0 0 24 24"><path d="M12 2a7 7 0 0 0-7 7c0 5 7 13 7 13s7-8 7-13a7 7 0 0 0-7-7zm0 9.5A2.5 2.5 0 1 1 12 6.5a2.5 2.5 0 0 1 0 5z"/></svg>
        <span class="contact-text">Mira Talven, lumo-thara, Lindenweg 14,<br>8857 Vorderthal (SZ)</span>
      </li>
      <li class="contact-item contact-item--phone">
        <svg class="contact-icon" viewBox="0 0 24 24"><path d="M6.6 10.8a15 15 0 0 0 6.6 6.6l2.2-2.2c.3-.3.7-.4 1-.2 1.1.4 2.3.6 3.6.6.6 0 1 .4 1 1V20c0 .6-.4 1-1 1A17 17 0 0 1 3 4c0-.6.4-1 1-1h3.5c.6 0 1 .4 1 1 0 1.3.2 2.5.6 3.6.1.3 0 .7-.2 1z"/></svg>
        <span class="contact-text">+41 77 000 12 34 (Bitte keine Werbung)</span>
      </li>
      <li class="contact-item contact-item--web">
        <svg class="contact-icon" viewBox="0 0 24 24"><path d="M12 2a10 10 0 1 0 0 20 10 10 0 0 0 0-20zm6.9 6h-3a15 15 0 0 0-1.3-3.9A8 8 0 0 1 18.9 8zM12 4c.8 1.1 1.5 2.5 1.9 4h-3.8c.4-1.5 1.1-2.9 1.9-4zM4.3 14a8 8 0 0 1 0-4h3.4a16 16 0 0 0 0 4zm.8 2h3a15 15 0 0 0 1.3 3.9A8 8 0 0 1 5.1 16zm3-8h-3a8 8 0 0 1 4.3-3.9A15 15 0 0 0 8.1 8zM12 20c-.8-1.1-1.5-2.5-1.9-4h3.8c-.4 1.5-1.1 2.9-1.9 4zm2.3-6H9.7a14 14 0 0 1 0-4h4.6a14 14 0 0 1 0 4zm.3 5.9a15 15 0 0 0 1.3-3.9h3a8 8 0 0 1-4.3 3.9zm1.7-5.9a16 16 0 0 0 0-4h3.4a8 8 0 0 1 0 4z"/></svg>
        <span class="contact-text">www.lumo-thara.ch</span>
      </li>
      <li class="contact-item contact-item--mail">
        <svg class="contact-icon" viewBox="0 0 24 24"><path d="M3 5h18v14H3zm2 2v.5l7 4.5 7-4.5V7zm0 2.9V17h14V9.9l-7 4.5z"/></svg>
        <span class="contact-text">info@lumo-thara.ch</span>
      </li>
    </ul>
  </section>
</body>
</html>
```